WE HAND MAKE AND DECORATE BEAUTIFUL CREATIVE GINGER BREAD HOUSES FOR CHRISTMAS AND CUPCAKES FOR SPECIAL OCCASIONS

Contact Information for Business Card

MAPLE AND THISTLE DESIGNS
FLORA 0467 213 809
BRENDA 0455038216

```html
<!DOCTYPE html>
<html lang="en">
<head>
<meta charset="utf-8">
<title>Maple &amp; Thistle Designs – Business Card</title>
<link rel="stylesheet" href="https://fonts.googleapis.com/css2?family=Lobster&family=Courgette&display=swap">
<style>
  :root {
    --page-bg: #e9e4df;
    --card-brown: #4b3630;
    --card-stripe: #533c35;
    --title-cream: #eadcd2;
    --text-white: #fbf7f3;
    --photo-frame: #f4f1ee;
    --photo-warm: #9a7a62;
    --photo-light: #d9d3cc;
  }
  html, body {
    margin: 0;
    width: 1200px;
    height: 1023px;
    overflow: hidden;
    background: var(--page-bg);
  }
  .stage {
    width: 1200px;
    height: 1023px;
    display: flex;
    align-items: center;
    justify-content: center;
  }
  .business-card {
    width: 540px;
    height: 920px;
    box-sizing: border-box;
    border-radius: 14px;
    background:
      repeating-linear-gradient(135deg,
        var(--card-brown) 0 14px,
        var(--card-stripe) 14px 28px);
    box-shadow: 0 10px 30px rgba(0,0,0,.25);
    display: flex;
    flex-direction: column;
    align-items: center;
    padding: 70px 40px 0;
    text-align: center;
  }
  .brand-name {
    margin: 0;
    font-family: "Lobster", cursive;
    font-weight: 400;
    font-size: 62px;
    line-height: 1.02;
    color: var(--title-cream);
  }
  .product-photo {
    margin-top: 34px;
    width: 330px;
    height: 232px;
    border-radius: 50%;
    border: 8px solid var(--photo-frame);
    box-sizing: border-box;
    background: radial-gradient(ellipse at 50% 60%, var(--photo-warm) 0%, #8a6a55 45%, var(--photo-light) 100%);
  }
  .tagline {
    margin: 72px 0 0;
    font-family: "Courgette", cursive;
    font-size: 26px;
    line-height: 1.22;
    color: var(--text-white);
  }
  .contact-list {
    margin-top: 62px;
    font-family: "Courgette", cursive;
    font-size: 40px;
    line-height: 1.35;
    color: var(--text-white);
  }
  .contact-line { display: block; }
</style>
</head>
<body>
  <main class="stage">
    <article class="business-card">
      <h1 class="brand-name">Maple &amp; Thistle<br>Designs</h1>
      <div class="product-photo" role="img" aria-label="Photo of a decorated gingerbread house with candy canes and icing"></div>
      <p class="tagline">We Hand make and decorate Beautiful Creative Ginger Bread Houses for Christmas and Cupcakes for Special Occasions.</p>
      <div class="contact-list">
        <span class="contact-line">Flora - 0467 213 809</span>
        <span class="contact-line">Brenda - 0455038216</span>
      </div>
    </article>
  </main>
</body>
</html>
```